Luxury Eco accommodation needs new website

Luxury lodge accommodation on exclusive private property in Flinders Ranges South Australia.
Brand new venture needs new site.
Focus on small group accommodation on exclusive property with outdoor experiences. Mountain biking , bush walking, outdoor dining.
We currently have a website but are having trouble making it our own. Needs to be "polished" by a professional.
Can you help?

www.larkhollowretreat.com.au

Target Market(s)

High income travellers, luxury accommodation

Industry/Entity Type

Accommodation

```html
<!DOCTYPE html>
<html lang="en">
<head>
<meta charset="utf-8">
<title>Lark Hollow Retreat – Wren Cottage</title>
<link rel="stylesheet" href="https://fonts.googleapis.com/css2?family=Josefin+Sans:wght@300;400&family=Questrial&display=swap">
<style>
  :root {
    --sidebar-bg: #ffffff;
    --column-bg: #221209;
    --column-text: #e9dccb;
    --column-muted: #cdbba6;
    --ink: #1a1a1a;
    --ink-soft: #3a3a3a;
    --dot: #4a4a4a;
    --dot-light: #b9a58c;
    --photo-frame: #4a3020;
  }
  * { box-sizing: border-box; margin: 0; padding: 0; }
  html, body { width: 1200px; height: 960px; overflow: hidden; }
  body {
    position: relative;
    font-family: "Questrial", sans-serif;
    color: var(--ink);
    background: linear-gradient(180deg, #c9d9dc 0%, #b88c6a 35%, #5a2d18 55%, #0b0b0b 80%, #000 100%);
  }
  .sidebar {
    position: absolute; left: 0; top: 0; width: 206px; height: 960px;
    background: var(--sidebar-bg);
  }
  .brand {
    position: absolute; left: 18px; top: 30px; width: 168px; height: 140px;
    display: flex; flex-direction: column; align-items: center; justify-content: flex-end;
    font-family: "Josefin Sans", sans-serif; font-weight: 300; color: #3d4447;
    text-transform: uppercase; text-align: center;
  }
  .brand-mark { width: 22px; height: 22px; background: #3d4447; margin-bottom: 26px; }
  .brand-name { font-size: 24px; letter-spacing: 2px; line-height: 1; }
  .brand-sub { font-size: 11px; letter-spacing: 9px; margin-top: 10px; padding-left: 9px; line-height: 1; }
  .main-nav {
    position: absolute; left: 0; top: 212px; width: 206px; list-style: none; text-align: center;
    font-family: "Josefin Sans", sans-serif; font-weight: 300; font-size: 17px;
    text-transform: uppercase; line-height: 26px; color: #333;
  }
  .dotted { position: absolute; border-top: 2px dotted var(--dot); height: 0; }
  .social { position: absolute; top: 392px; width: 22px; height: 22px; border-radius: 50%; background: #000; }
  .contact {
    position: absolute; right: 20px; top: 461px; width: 180px; text-align: right;
    font-size: 13.5px; line-height: 17px; color: #333;
  }
  .contact p + p { margin-top: 17px; }

  .info-column {
    position: absolute; left: 206px; top: 0; width: 206px; height: 960px;
    background: var(--column-bg); color: var(--column-text); text-align: center;
  }
  .column-heading {
    position: absolute; left: 0; width: 206px;
    font-family: "Josefin Sans", sans-serif; font-weight: 300; font-size: 17px;
    text-transform: uppercase; line-height: 1;
  }
  .info-column .dotted { left: 26px; width: 155px; border-top-color: var(--dot-light); }
  .gallery-photo {
    position: absolute; left: 26px; top: 97px; width: 155px; height: 187px;
    border: 4px solid var(--photo-frame);
    background: linear-gradient(180deg, #9fb7d2 0%, #d8dde2 35%, #8a8c84 55%, #8b7a5c 75%, #7b6a4c 100%);
  }
  .slider-dots { position: absolute; left: 57px; top: 300px; display: flex; gap: 10px; }
  .slider-dots span { width: 9px; height: 9px; background: #4a3628; }
  .slider-dots span.active { background: transparent; border: 1px solid #6b5443; }
  .testimonial {
    position: absolute; left: 26px; top: 396px; width: 155px;
    font-size: 13px; line-height: 17px; color: var(--column-muted);
  }
  .testimonial cite { display: block; margin-top: 17px; font-style: normal; }
  .downloads {
    position: absolute; left: 0; top: 680px; width: 206px; list-style: none;
    font-family: "Josefin Sans", sans-serif; font-weight: 300; font-size: 17px;
    text-transform: uppercase; line-height: 30px;
  }

  .content {
    position: absolute; left: 412px; top: 3px; width: 718px; height: 957px;
    background: linear-gradient(180deg, #fbfbfb 0%, #f2f0ee 20%, #e6e6e6 55%, #d9d9d9 100%);
    box-shadow: 0 0 12px rgba(0,0,0,0.15);
    text-align: center;
  }
  .page-title {
    position: absolute; left: 0; top: 34px; width: 100%;
    font-family: "Josefin Sans", sans-serif; font-weight: 400; font-size: 22px;
    text-transform: uppercase; letter-spacing: 0.5px; line-height: 1;
  }
  .title-flourish { position: absolute; left: 344px; top: 66px; width: 66px; height: 10px; background: #5a5a5a; border-radius: 5px; opacity: .55; }
  .intro {
    position: absolute; left: 38px; top: 114px; width: 642px;
    font-size: 14.5px; line-height: 18.75px; color: var(--ink);
  }
  .hero {
    position: absolute; left: 38px; top: 211px; width: 641px; height: 365px; display: flex;
  }
  .hero-left { width: 240px; height: 100%; background: linear-gradient(180deg, #7f7560 0%, #d2c3ad 40%, #6d6a60 75%, #bdb0a0 100%); }
  .hero-right { flex: 1; height: 100%; background: linear-gradient(180deg, #b7bcbc 0%, #d9d6cc 35%, #7c8a6a 60%, #c9bfae 100%); }
  .detail {
    position: absolute; left: 38px; width: 642px;
    font-size: 14.5px; line-height: 18.75px;
  }
</style>
</head>
<body>
  <aside class="sidebar">
    <div class="brand">
      <span class="brand-mark"></span>
      <span class="brand-name">Lark Hollow</span>
      <span class="brand-sub">Retreat</span>
    </div>
    <ul class="main-nav">
      <li>Luxury Lodge</li>
      <li>Other Stays</li>
      <li>Experiences</li>
      <li>Gallery</li>
      <li>Contact</li>
    </ul>
    <div class="dotted" style="left:55px;top:380px;width:96px;"></div>
    <span class="social" style="left:73px;" aria-label="Social link"></span>
    <span class="social" style="left:106px;" aria-label="Social link"></span>
    <div class="dotted" style="left:67px;top:423px;width:73px;"></div>
    <div class="contact">
      <p>Somewhere road 123<br>info@larkhollow.com<br>Contact – (08) 5550 2417</p>
      <p>Copyright<br>larkhollowretreat<br>2013</p>
    </div>
  </aside>

  <section class="info-column">
    <h2 class="column-heading" style="top:46px;">Gallery</h2>
    <div class="dotted" style="top:75px;"></div>
    <div class="gallery-photo" role="img" aria-label="Modern lodge building on a grassy hillside under a cloudy sky"></div>
    <div class="slider-dots"><span class="active"></span><span></span><span></span><span></span><span></span><span></span></div>
    <h2 class="column-heading" style="top:347px;">Testimonial</h2>
    <div class="dotted" style="top:376px;"></div>
    <blockquote class="testimonial">
      Lorem ipsum dolor sit amet, consectetur adipisic­ing elit, sed do eiusmod tempor incididunt ut labore et dolore magna aliqua. Ut enim ad minim veniam, quis nostrud exercitation ullamco laboris nisi ut aliquip ex ea commodo consequat.,
      <cite>~ Mara ~</cite>
    </blockquote>
    <h2 class="column-heading" style="top:633px;">Download PDF</h2>
    <div class="dotted" style="top:662px;"></div>
    <ul class="downloads">
      <li>Rates / Price</li>
      <li>Accomodation</li>
      <li>Catering</li>
    </ul>
  </section>

  <main class="content">
    <h1 class="page-title">Wren Cottage</h1>
    <div class="title-flourish" role="img" aria-label="Decorative flourish"></div>
    <p class="intro">Wren Cottage is a fully restored miner's cottage constructed of native pine and local stone.<br>The cottage offers a cosy and comfortable environment from which to enjoy visiting the Tarrawong district. The cottage restoration, through the use of timber and local materials, offers an intimacy and a strong connection with the history of the area</p>
    <div class="hero">
      <div class="hero-left" role="img" aria-label="Guests relaxing on the cottage verandah"></div>
      <div class="hero-right" role="img" aria-label="Stone cottage with verandah and white picket fence"></div>
    </div>
    <p class="detail" style="top:612px;">Charming 1870's miners cottage, fully restored in the main street of Tarrawong.</p>
    <p class="detail" style="top:668px;">Two bedroom air-conditioned cottage with wood burning heater &nbsp;and all the luxuries of home.<br>Located in the main street of the tiny town of Tarrawong, walk to local shops, cafe and hotel.<br>Great base for exploring the Flinders Ranges.</p>
  </main>
</body>
</html>
```